Business Card Re-Design Project

I need to re-design my business card. I run a creative studio specializing in Media production, Web design, and Mobile Applications. I don't like my old one and I am looking for a creative way to rebrand my business card. I am open to materials other than paper - (e.g. PVC plastic).
This business card should be versatile and I can pass it out to anyone but not just clients who need my service, it should be a good networking card, not a card about what service I provide.
Target Market(s)
Upscale clients, banks, fashion company
Industry/Entity Type
Business
Requirements
Must have
- Bi-Lingual in English and Chinese, QR Code
File must be ready to print
Nice to have
- Anything that makes the business card more than just a business card
Should not have
- Must not have any old school and cliche logos such as a camera logo. Because we are a creative studio and we don't just specialize on one thing.
Must not have undersized font. My old business card's font is too hard to read!

```html
<!DOCTYPE html>
<html lang="en">
<head>
<meta charset="utf-8">
<title>Kavron Business Card</title>
<link href="https://fonts.googleapis.com/css2?family=Cinzel:wght@400&family=Open+Sans:wght@400;700&family=Noto+Serif+TC:wght@400&display=swap" rel="stylesheet">
<style>
  :root {
    --bg: #1b1c1d;
    --row: #232527;
    --row-line: #151617;
    --white: #ffffff;
    --gold: #f4b400;
    --icon-dim: #3a3c3e;
    --qr-frame: #2c2e30;
  }
  html, body {
    margin: 0;
    padding: 0;
    overflow: hidden;
    background: var(--bg);
  }
  .card {
    position: relative;
    width: 1200px;
    height: 668px;
    background: var(--bg);
    overflow: hidden;
    font-family: "Open Sans", sans-serif;
    color: var(--white);
  }
  .brand {
    position: absolute;
    left: 336px;
    top: 138px;
    width: 372px;
    font-weight: 700;
    font-size: 70px;
    line-height: 1;
    letter-spacing: 8px;
    color: var(--white);
    white-space: nowrap;
  }
  .spine {
    position: absolute;
    left: 338px;
    top: 225px;
    width: 11px;
    height: 443px;
    background: var(--white);
  }
  .row {
    position: absolute;
    left: 270px;
    width: 483px;
    background: var(--row);
    border-top: 2px solid var(--row-line);
  }
  .row-phone-us { top: 330px; height: 73px; }
  .row-phone-hk { top: 405px; height: 73px; }
  .row-web { top: 480px; height: 70px; }
  .row-mail { top: 552px; height: 71px; }
  .row-icon {
    position: absolute;
    left: 18px;
    width: 30px;
    height: 30px;
  }
  .row-text {
    position: absolute;
    left: 92px;
    font-size: 18px;
    white-space: nowrap;
  }
  .label { color: var(--gold); }
  .address-icon {
    position: absolute;
    left: 286px;
    top: 236px;
    width: 30px;
    height: 30px;
  }
  .address {
    position: absolute;
    left: 362px;
    top: 242px;
    font-size: 29px;
    line-height: 38px;
    margin: 0;
    white-space: nowrap;
  }
  .person-icon {
    position: absolute;
    left: 942px;
    top: 268px;
    width: 38px;
    height: 40px;
  }
  .name {
    position: absolute;
    right: 72px;
    top: 326px;
    margin: 0;
    font-family: "Cinzel", serif;
    font-weight: 400;
    font-size: 52px;
    line-height: 1;
    white-space: nowrap;
  }
  .name .surname { color: var(--gold); }
  .title {
    position: absolute;
    right: 72px;
    top: 390px;
    margin: 0;
    font-family: "Cinzel", serif;
    font-size: 33px;
    letter-spacing: 5px;
    color: var(--gold);
    line-height: 1;
    white-space: nowrap;
  }
  .name-zh {
    position: absolute;
    right: 74px;
    top: 440px;
    margin: 0;
    font-family: "Noto Serif TC", serif;
    font-size: 24px;
    letter-spacing: 6px;
    line-height: 1;
    color: var(--white);
    white-space: nowrap;
  }
  .name-zh .title-zh { color: var(--gold); }
  .qr {
    position: absolute;
    right: 76px;
    top: 500px;
    width: 116px;
    height: 116px;
    background: var(--white);
    border: 6px solid var(--qr-frame);
  }
</style>
</head>
<body>
<div class="card">
  <div class="brand">KAVRON</div>

  <svg class="address-icon" viewBox="0 0 30 30" aria-hidden="true">
    <path d="M15 3 L2 15 H6 V27 H12 V19 H18 V27 H24 V15 H28 Z" fill="none" stroke="var(--gold)" stroke-width="3" stroke-linejoin="round"/>
  </svg>
  <p class="address">120 Marlow Ave Suite #210<br>Irvine CA 92600</p>

  <div class="row row-phone-us">
    <svg class="row-icon" style="top:20px" viewBox="0 0 30 30" aria-hidden="true">
      <path d="M9 3 C6 4 4 7 5 11 C7 18 12 24 19 27 C22 28 25 26 26 23 L21 19 L18 22 C14 20 11 16 9 12 L12 9 Z" fill="var(--icon-dim)"/>
    </svg>
    <span class="row-text" style="top:22px"><span class="label">US Phone :</span> +1 (555) 014-2270</span>
  </div>

  <div class="row row-phone-hk">
    <svg class="row-icon" style="top:20px" viewBox="0 0 30 30" aria-hidden="true">
      <path d="M9 3 C6 4 4 7 5 11 C7 18 12 24 19 27 C22 28 25 26 26 23 L21 19 L18 22 C14 20 11 16 9 12 L12 9 Z" fill="var(--white)"/>
    </svg>
    <span class="row-text" style="top:22px"><span class="label">HK Phone :</span> +852 5550-1234</span>
  </div>

  <div class="row row-web">
    <svg class="row-icon" style="top:20px" viewBox="0 0 30 30" aria-hidden="true">
      <circle cx="11" cy="11" r="5" fill="var(--icon-dim)"/>
      <path d="M2 26 C2 19 6 17 11 17 C16 17 20 19 20 26 Z" fill="var(--icon-dim)"/>
      <circle cx="21" cy="13" r="4" fill="var(--icon-dim)"/>
      <path d="M22 26 C22 22 21 20 19 19 C24 18 28 20 28 26 Z" fill="var(--icon-dim)"/>
    </svg>
    <span class="row-text" style="top:22px">www.kavron.com</span>
  </div>

  <div class="row row-mail">
    <svg class="row-icon" style="top:14px" viewBox="0 0 30 30" aria-hidden="true">
      <rect x="3" y="7" width="24" height="16" fill="var(--icon-dim)"/>
      <path d="M3 7 L15 17 L27 7" fill="none" stroke="var(--row)" stroke-width="2"/>
    </svg>
    <span class="row-text" style="top:12px">dorian.lo@kavron.com</span>
  </div>

  <div class="spine"></div>

  <svg class="person-icon" viewBox="0 0 38 40" aria-hidden="true">
    <circle cx="19" cy="11" r="9" fill="var(--gold)"/>
    <path d="M2 40 C2 27 9 22 19 22 C29 22 36 27 36 40 Z" fill="var(--gold)"/>
    <path d="M17 23 L21 23 L20 33 L18 33 Z" fill="var(--bg)"/>
  </svg>
  <h1 class="name">DORIAN <span class="surname">LO</span></h1>
  <p class="title">PRINCIPAL</p>
  <p class="name-zh" lang="zh-Hant">羅多年 <span class="title-zh">負責人</span></p>

  <div class="qr" role="img" aria-label="QR code linking to www.kavron.com"></div>
</div>
</body>
</html>
```